K-12 Education site

We are looking for a Wordpress theme that does the following:
- Uses our school colors: green and gold/yellow (not a true requirement as these colors can be pretty ugly)
- Works on all mobile devices and scales properly
- We are an Arts and Technology school so we would like the design to be clean, vibrant, and yet make use of HTML5
- Unique design

Target Market(s)

Prospective students and current students

Industry/Entity Type

School

Requirements
Must have
• Clean and unique Design
HTML5
Must scale for mobile devices

```html
<!DOCTYPE html>
<html lang="en">
<head>
<meta charset="utf-8">
<title>Riverbend Regional Arts School</title>
<link href="https://fonts.googleapis.com/css2?family=Roboto:wght@400;500;700&display=swap" rel="stylesheet">
<style>
:root{
  --gold:#e8990c;
  --green:#1f6a40;
  --green-dark:#17532f;
  --red:#b3193f;
  --heading:#555a5e;
  --text:#6b6b6b;
  --rule:#d6d6d6;
  --footer:#eeeeee;
  --white:#ffffff;
}
*{margin:0;padding:0;box-sizing:border-box}
html,body{width:1067px;height:1200px;overflow:hidden;background:var(--white);font-family:"Roboto",Arial,sans-serif;color:var(--text)}
.page{position:relative;width:1067px;height:1200px}
.abs{position:absolute}
.brand{left:107px;top:62px;display:flex;align-items:center;gap:8px;font-size:19px;font-weight:700;color:var(--green)}
.brand .mark{width:16px;height:16px;background:var(--gold)}
.brand small{display:block;font-size:9px;font-weight:500;color:var(--text);letter-spacing:1px}
.search{left:736px;top:40px;width:224px;height:33px;border:1px solid #ccc;border-radius:2px;box-shadow:inset 0 1px 3px rgba(0,0,0,.1)}
.search svg{position:absolute;right:8px;top:9px}
.search .sep{position:absolute;right:30px;top:5px;width:1px;height:21px;background:#ddd}
.social{left:810px;top:96px;display:flex;gap:6px}
.social span{width:25px;height:25px;background:#8a8f93}
.band{left:0;top:177px;width:1067px;height:409px;background:var(--gold)}
.nav{left:106px;top:161px;width:853px;height:35px;background:var(--green);display:flex;border-bottom:2px solid var(--green-dark);border-radius:2px}
.nav a{color:var(--white);text-decoration:none;font-size:11px;font-weight:700;line-height:35px;padding:0 13px;white-space:nowrap}
.nav a.active{background:var(--gold);padding:0 10px}
.slider{left:107px;top:212px;width:853px;height:337px;background:linear-gradient(180deg,#b9a48a 0%,#2f5a3f 55%,#9a7245 100%)}
.slider-shadow{left:120px;top:549px;width:827px;height:18px;border-radius:0 0 50% 50%;background:rgba(0,0,0,.25);filter:blur(4px)}
.dots{left:478px;top:530px;width:112px;height:19px;background:rgba(200,200,200,.8);border-radius:4px 4px 0 0;display:flex;justify-content:center;align-items:center;gap:5px}
.dots i{width:8px;height:8px;border-radius:50%;background:#999;display:block}
.dots i.on{background:#444}
h2{font-size:16.5px;font-weight:500;color:var(--heading);text-transform:uppercase;letter-spacing:.2px}
h2 em{font-style:normal;color:var(--gold)}
.btn{display:inline-block;background:var(--red);color:var(--white);font-size:11.5px;font-weight:700;padding:0 6px;height:29px;line-height:29px;border-radius:2px;box-shadow:0 2px 2px rgba(0,0,0,.2)}
p.body{font-size:10.5px;line-height:16px;text-align:justify}
.vrule{left:678px;top:603px;width:2px;height:228px;background:var(--rule)}
.hrule{left:106px;top:865px;width:853px;height:3px;background:var(--rule)}
.news-item{display:flex;gap:9px;font-size:10px;line-height:12.5px}
.news-item .thumb{width:71px;height:63px;flex:none}
.news-item b{color:var(--gold);font-weight:500;font-size:11px;display:block}
.news-item .date{font-size:11.5px;color:#555;display:block;margin:2px 0 1px}
.footer{left:0;top:1156px;width:1067px;height:44px;background:var(--footer);font-size:10.5px;color:#888;line-height:44px}
</style>
</head>
<body>
<div class="page">
  <div class="abs brand"><span class="mark"></span><div>RIVERBEND<small>MILLBROOK, VA</small></div></div>
  <div class="abs search"><span class="sep"></span>
    <svg width="12" height="12" viewBox="0 0 12 12"><circle cx="5" cy="5" r="3.5" fill="none" stroke="#aaa" stroke-width="1.5"/><line x1="7.5" y1="7.5" x2="11" y2="11" stroke="#aaa" stroke-width="1.8"/></svg>
  </div>
  <div class="abs social"><span></span><span></span><span></span><span></span><span></span></div>

  <div class="abs band"></div>
  <nav class="abs nav">
    <a class="active">HOME</a><a>DISCOVER RRAS</a><a>STUDENTS/PARENTS</a><a>FACULTY/STAFF</a><a>DOCUMENTS/FORMS</a><a>PROGRAMS OF STUDY</a><a>SERVICES</a><a>CONTACT US</a>
  </nav>
  <div class="abs slider-shadow"></div>
  <div class="abs slider" role="img" aria-label="Photo of the dance team posing in the school gym with a trophy"></div>
  <div class="abs dots"><i></i><i></i><i class="on"></i><i></i><i></i><i></i></div>

  <h2 class="abs" style="left:107px;top:602px">Welcome to <em>Riverbend Regional Arts School!</em></h2>
  <div class="abs" role="img" aria-label="Photo of a student performing in a school play" style="left:107px;top:647px;width:213px;height:140px;background:linear-gradient(90deg,#23406e 0%,#3b5c8c 45%,#b87a48 75%,#7a4a2e 100%)"></div>
  <div class="abs" style="left:336px;top:643px;width:331px">
    <p class="body">Sed ut perspiciatis unde omnis iste natus error sit voluptatem accusantium doloremque laudantium, totam rem aperiam, eaque ipsa quae ab illo inventore</p>
    <p class="body" style="margin-top:16px">Lorem ipsum dolor sit amet, consectetur adipisicing elit, sed do eiusmod tempor incididunt ut labore et dolore magna aliqua. Ut enim ad minim veniam, quis nostrud exercitation ullamco laboris nisi ut aliquip ex ea commodo consequat. Duis aute irure dolor in reprehenderit in voluptate velit esse cillum dolore eu fugiat nulla pariatur. Excepteur sint</p>
  </div>
  <a class="abs btn" style="left:107px;top:804px">READ MORE</a>

  <div class="abs vrule"></div>
  <h2 class="abs" style="left:693px;top:602px">Latest News</h2>
  <div class="abs" style="left:693px;top:646px;width:270px">
    <div class="news-item"><div class="thumb" role="img" aria-label="Photo of a smiling office worker" style="background:linear-gradient(90deg,#dfe3e6,#3a3a3a)"></div>
      <div><b>Parents: Received a letter about electronic forms</b><span class="date">08 August, 2013</span>Lorem ipsum dolor sit amet, consectetur adipisicing elit, sed do eiusmod</div></div>
    <div class="news-item" style="margin-top:19px"><div class="thumb" role="img" aria-label="Photo of a group of staff members" style="background:linear-gradient(90deg,#8a7a6a,#2c2c2c)"></div>
      <div><b>Parents: Received a letter about electronic forms</b><span class="date">08 August, 2013</span>Lorem ipsum dolor sit amet, consectetur adipisicing elit, sed do eiusmod</div></div>
  </div>
  <a class="abs btn" style="left:693px;top:804px">READ MORE</a>

  <div class="abs hrule"></div>

  <h2 class="abs" style="left:107px;top:893px">Faculty and Staff</h2>
  <div class="abs" role="img" aria-label="Photo of four smiling teachers outdoors" style="left:107px;top:933px;width:267px;height:98px;background:linear-gradient(180deg,#c9dcef,#6a5040)"></div>
  <p class="abs body" style="left:107px;top:1039px;width:268px">This section of the RRAS Website will provide you with some useful information about RRAS and the technologies used along with links to various locations that you may find useful.</p>
  <a class="abs btn" style="left:107px;top:1109px">READ MORE</a>

  <h2 class="abs" style="left:400px;top:893px">RRAS Students</h2>
  <div class="abs" role="img" aria-label="Photo of students seated on gym bleachers" style="left:401px;top:933px;width:267px;height:98px;background:linear-gradient(180deg,#9a5a34,#6a3e2a)"></div>
  <p class="abs body" style="left:401px;top:1039px;width:268px">This section of the RRAS Website will provide you with some useful information about RRAS and the technologies used along with links to various locations that you may find useful.</p>
  <a class="abs btn" style="left:400px;top:1109px">READ MORE</a>

  <h2 class="abs" style="left:693px;top:893px">Our Mission</h2>
  <div class="abs" role="img" aria-label="Photo of hands working on a colourful art project" style="left:694px;top:933px;width:267px;height:98px;background:linear-gradient(90deg,#f6eedc,#e9c08a,#f4efe6)"></div>
  <p class="abs body" style="left:694px;top:1039px;width:268px">This section of the RRAS Website will provide you with some useful information about RRAS and the technologies used along with links to various locations that you may find useful.</p>
  <a class="abs btn" style="left:693px;top:1109px">READ MORE</a>

  <footer class="abs footer">
    <span class="abs" style="left:107px">© 2013 Riverbend Regional Arts School |</span>
    <span class="abs" style="left:861px">Privacy Policy | Terms</span>
  </footer>
</div>
</body>
</html>
```